Pull Up Banner Design 85cm X200cm

The pull up banner is intended for branding and services awareness purposes, and to be used at exhibition and conference. Please refer to the websites below for more information
1. https://www.advisory-nook.net/
2. https://www.advisory-nook.net/landing-page
3. https://blog.advisory-nook.net/faq-for-client/
4. https://blog.advisory-nook.net/faq-for-advisor/

Ideally, the banner will lead potential users both young entrepreneurs and online business owners (as clients) to Brivana Hub marketplace, and also professional services providers like accountants and finance advisors and consultants (as advisors) to sign up with the platform. (Like ArtForge marketplace)

Target Market(s)

Business users and accountants aged between 25 to 44 yrs old

Requirements
Must have
• website address (www.advisory-nook.net)
• and
• company logo "Brivana Hub" as attached

```html
<!DOCTYPE html>
<html lang="en">
<head>
<meta charset="utf-8">
<title>Brivana Hub – Pull Up Banner</title>
<link rel="stylesheet" href="https://fonts.googleapis.com/css2?family=Open+Sans:wght@400;600;700;800&display=swap">
<style>
  :root {
    --brand-blue: #1670bf;
    --brand-blue-deep: #0f62ad;
    --ink: #2f3439;
    --ink-soft: #4a5056;
    --band-gray: #50565c;
    --sky-top: #e4f0f9;
    --sky-bottom: #f5fafd;
    --stage: #e9ecef;
    --white: #ffffff;
    --icon-teal: #4fd1c5;
    --icon-orange: #f7a81b;
  }
  * { margin: 0; padding: 0; box-sizing: border-box; }
  html, body { width: 1200px; height: 2250px; overflow: hidden; }
  body {
    background: var(--stage);
    font-family: "Open Sans", Arial, sans-serif;
    color: var(--ink);
  }
  .banner {
    position: absolute;
    left: 122px; top: 0;
    width: 956px; height: 2250px;
    overflow: hidden;
    background: linear-gradient(160deg, var(--sky-top), var(--sky-bottom) 45%, #e6f2fa);
  }
  .shapes, .team-photo { position: absolute; left: 0; top: 0; width: 956px; height: 2250px; }
  .brand-dot {
    position: absolute; left: 403px; top: 86px;
    width: 150px; height: 150px; border-radius: 50%;
    background: var(--brand-blue);
  }
  .brand-name {
    position: absolute; left: 0; right: 0; top: 252px;
    text-align: center;
    font-size: 80px; font-weight: 600; line-height: 92px;
    color: var(--brand-blue);
  }
  .tagline {
    position: absolute; left: 0; right: 0; top: 365px;
    text-align: center; font-size: 36px; line-height: 54px;
    color: var(--ink);
  }
  .tagline strong { font-weight: 700; }
  .tagline .hl { font-weight: 700; color: var(--brand-blue); }
  .headline {
    position: absolute; left: 119px; top: 1164px;
    font-size: 69px; font-weight: 800; line-height: 73px; letter-spacing: 0.5px;
    white-space: nowrap;
  }
  .headline .line-blue { color: var(--brand-blue); display: block; }
  .headline .line-dark { color: var(--ink-soft); display: block; }
  .section-title {
    position: absolute; left: 119px;
    font-size: 55px; font-weight: 400; color: var(--ink-soft); line-height: 70px;
    white-space: nowrap;
  }
  .section-title b { font-weight: 800; color: var(--brand-blue-deep); }
  .title-rule {
    position: absolute; left: 119px; width: 146px; height: 6px;
    background: var(--brand-blue);
  }
  .feature-icon { position: absolute; }
  .feature-label {
    position: absolute; width: 320px; white-space: nowrap;
    font-weight: 700; color: var(--ink-soft);
  }
  .feature-label span { display: block; color: var(--brand-blue); }
  .feature-label.inline span { display: inline; }
  .advisor { font-size: 28px; line-height: 38px; top: 1564px; }
  .project { font-size: 33px; line-height: 42px; top: 1850px; }
  .site-url {
    position: absolute; left: 0; right: 0; top: 2095px;
    text-align: center; font-size: 64px; line-height: 90px; font-weight: 400; color: var(--white);
  }
</style>
</head>
<body>
<main class="banner">
  <svg class="team-photo" viewBox="0 0 956 2250" role="img" aria-label="Photo of four young professionals discussing work around a laptop in a bright office">
    <defs>
      <linearGradient id="photoTone" x1="0" y1="0" x2="0" y2="1">
        <stop offset="0" stop-color="#c9d3db" stop-opacity="0"/>
        <stop offset="0.18" stop-color="#c9d3db"/>
        <stop offset="0.6" stop-color="#b5bfc8"/>
        <stop offset="1" stop-color="#9fa9b4"/>
      </linearGradient>
    </defs>
    <path d="M0 493 H956 V1000 C650 1060 300 1010 0 930 Z" fill="url(#photoTone)"/>
  </svg>

  <svg class="shapes" viewBox="0 0 956 2250" aria-hidden="true">
    <path d="M0 930 C300 1010 650 1060 956 1000 L956 1030 C650 1100 300 1110 0 1020 Z" fill="var(--brand-blue)"/>
    <path d="M0 1020 C300 1110 650 1100 956 1030 L956 1046 C650 1110 300 1150 0 1078 Z" fill="var(--band-gray)"/>
    <path d="M0 1990 C300 1985 650 1965 956 1868 L956 2250 L0 2250 Z" fill="var(--band-gray)"/>
    <path d="M0 2005 C300 2000 650 1980 956 1910 L956 2250 L0 2250 Z" fill="var(--white)"/>
    <path d="M0 2016 C300 2010 650 1990 956 1925 L956 2250 L0 2250 Z" fill="var(--brand-blue)"/>
  </svg>

  <div class="brand-dot"></div>
  <div class="brand-name">Brivana Hub</div>

  <p class="tagline">
    Join the ASEAN’s <span class="hl">FIRST</span> and most<br>
    <strong>credible network</strong> of <span class="hl">ACCOUNTING, TAX,</span><br>
    and <span class="hl">FINANCE</span> professionals
  </p>

  <h1 class="headline">
    <span class="line-blue">ENTREPRENEURSHIP</span>
    <span class="line-dark">EMPOWERED</span>
  </h1>

  <h2 class="section-title" style="top:1332px">Looking for an <b>ADVISOR?</b></h2>
  <div class="title-rule" style="top:1414px"></div>

  <svg class="feature-icon" style="left:119px; top:1450px" width="100" height="100" viewBox="0 0 110 110" aria-hidden="true">
    <circle cx="55" cy="55" r="52" fill="var(--icon-teal)"/>
    <rect x="22" y="30" width="66" height="46" rx="4" fill="#ffffff" stroke="#2f3439" stroke-width="3"/>
    <rect x="22" y="26" width="66" height="12" fill="#e84a4a"/>
    <circle cx="55" cy="57" r="9" fill="#e84a4a"/>
  </svg>
  <div class="feature-label advisor" style="left:119px">One-stop borderless<span>Marketplace</span></div>

  <svg class="feature-icon" style="left:444px; top:1450px" width="100" height="100" viewBox="0 0 110 110" aria-hidden="true">
    <circle cx="55" cy="55" r="52" fill="var(--icon-teal)"/>
    <circle cx="64" cy="28" r="8" fill="var(--brand-blue)"/>
    <path d="M60 40 L48 62 L62 72 L56 90 M48 62 L34 74 M58 46 L76 56 M56 44 L40 44" stroke="var(--brand-blue)" stroke-width="8" stroke-linecap="round" fill="none"/>
  </svg>
  <div class="feature-label advisor" style="left:444px">Convenient<span>and Quick</span></div>

  <svg class="feature-icon" style="left:696px; top:1450px" width="100" height="100" viewBox="0 0 110 110" aria-hidden="true">
    <circle cx="55" cy="55" r="52" fill="var(--icon-teal)"/>
    <rect x="24" y="50" width="14" height="36" fill="var(--brand-blue)"/>
    <path d="M42 50 L54 26 C60 22 64 28 62 36 L60 46 L80 46 C86 46 88 52 86 56 L80 84 L42 84 Z" fill="var(--icon-orange)"/>
  </svg>
  <div class="feature-label advisor" style="left:696px">Hire with<span>Confidence</span></div>

  <h2 class="section-title" style="top:1659px">Looking for a <b>PROJECT?</b></h2>
  <div class="title-rule" style="top:1740px"></div>

  <svg class="feature-icon" style="left:119px; top:1772px" width="100" height="72" viewBox="0 0 100 72" aria-hidden="true">
    <rect x="4" y="4" width="92" height="64" rx="6" fill="var(--icon-orange)"/>
    <circle cx="30" cy="30" r="10" fill="var(--brand-blue)"/>
    <path d="M14 56 C14 42 46 42 46 56 Z" fill="var(--brand-blue)"/>
    <rect x="54" y="22" width="34" height="6" fill="#ffffff"/>
    <rect x="54" y="36" width="34" height="6" fill="#ffffff"/>
    <rect x="54" y="50" width="24" height="6" fill="#ffffff"/>
  </svg>
  <div class="feature-label project" style="left:119px">Professional<span>Profile</span></div>

  <svg class="feature-icon" style="left:444px; top:1772px" width="100" height="72" viewBox="0 0 100 80" aria-hidden="true">
    <rect x="4" y="2" width="52" height="38" rx="3" fill="var(--brand-blue)"/>
    <rect x="62" y="8" width="36" height="44" rx="3" fill="var(--icon-teal)"/>
    <rect x="30" y="42" width="40" height="34" rx="3" fill="var(--icon-orange)"/>
    <circle cx="80" cy="28" r="9" fill="#ffffff"/>
  </svg>
  <div class="feature-label project" style="left:444px">Expertise<span>Showcase</span></div>

  <svg class="feature-icon" style="left:696px; top:1772px" width="110" height="72" viewBox="0 0 110 80" aria-hidden="true">
    <rect x="4" y="24" width="84" height="30" rx="15" fill="var(--brand-blue)"/>
    <rect x="16" y="36" width="58" height="6" fill="#ffffff"/>
    <path d="M84 6 L100 2 L96 18 Z" fill="var(--icon-orange)"/>
    <path d="M54 56 L44 70 L52 70 L46 80 L60 66 L52 66 Z" fill="#f5d90a"/>
  </svg>
  <div class="feature-label project inline" style="left:696px">Job <span>Leads</span></div>

  <div class="site-url">www.advisory-nook.net</div>
</main>
</body>
</html>
```